St. Calvarn inspired Gin label

To celebrate 'St Calvarns Day' we would like a gin label designed for a 50cl bottle with the alcohol ABV being 40%.<br/>I will upload a file displaying the types of bottles we would use and our gin company logo.

Font styles to use
Decorative

Colors
3176b5
ec1f27

```html
<!DOCTYPE html>
<html lang="en">
<head>
<meta charset="utf-8">
<title>St. Calvarn Gin Label</title>
<link rel="stylesheet" href="https://fonts.googleapis.com/css2?family=UnifrakturMaguntia&family=Cormorant+Garamond:wght@500;600&display=swap">
<style>
  :root {
    --backdrop: #8a97a8;
    --label-red: #d9646b;
    --label-blue: #3d9ad6;
    --label-blue-deep: #2f86c4;
    --ink-white: #ffffff;
    --ink-dark: #2a2426;
    --crest-light: #eef0f2;
    --crest-dark: #1e1c1e;
  }
  html, body {
    margin: 0;
    padding: 0;
    width: 1200px;
    height: 1028px;
    overflow: hidden;
    background: var(--backdrop);
  }
  .canvas {
    position: relative;
    width: 1200px;
    height: 1028px;
    background: var(--backdrop);
  }
  .gin-label {
    position: absolute;
    left: 330px;
    top: 146px;
    width: 540px;
    height: 736px;
    overflow: hidden;
  }
  .label-field {
    position: absolute;
    inset: 0;
  }
  .maker-mark {
    position: absolute;
    top: 80px;
    left: 0;
    width: 100%;
    display: flex;
    justify-content: center;
    align-items: center;
    gap: 10px;
    font-family: "Cormorant Garamond", serif;
    font-weight: 600;
    font-size: 16px;
    letter-spacing: 2px;
    text-transform: uppercase;
    color: var(--ink-dark);
  }
  .maker-mark__dot {
    width: 14px;
    height: 14px;
    border-radius: 50%;
    border: 2px solid var(--ink-dark);
  }
  .product-name {
    position: absolute;
    top: 206px;
    left: 0;
    width: 100%;
    margin: 0;
    text-align: center;
    font-family: "UnifrakturMaguntia", serif;
    font-weight: 400;
    font-size: 66px;
    line-height: 1;
    color: var(--ink-white);
  }
  .crest {
    position: absolute;
    left: 146px;
    top: 303px;
    width: 248px;
    height: 330px;
  }
  .volume {
    position: absolute;
    left: 50px;
    top: 660px;
    font-family: "UnifrakturMaguntia", serif;
    font-size: 44px;
    line-height: 1;
    color: var(--ink-white);
  }
  .strength {
    position: absolute;
    right: 16px;
    top: 668px;
    font-family: "UnifrakturMaguntia", serif;
    font-size: 36px;
    line-height: 1;
    color: var(--ink-white);
  }
</style>
</head>
<body>
  <main class="canvas">
    <section class="gin-label">
      <svg class="label-field" width="540" height="736" viewBox="0 0 540 736" aria-hidden="true">
        <defs>
          <linearGradient id="blueField" x1="0" y1="0" x2="0" y2="1">
            <stop offset="0" stop-color="var(--label-blue)"/>
            <stop offset="1" stop-color="var(--label-blue-deep)"/>
          </linearGradient>
        </defs>
        <rect width="540" height="736" fill="url(#blueField)"/>
        <polygon points="0,0 540,0 0,716" fill="var(--label-red)"/>
      </svg>

      <div class="maker-mark">
        <span class="maker-mark__dot"></span>
        <span>Hollowmere Gin Company</span>
      </div>

      <h1 class="product-name">St. Calvarn Gin</h1>

      <svg class="crest" viewBox="0 0 250 332" role="img" aria-label="Emblem area: heraldic shield illustration in black, white and red">
        <defs>
          <linearGradient id="crestTone" x1="0" y1="0" x2="1" y2="1">
            <stop offset="0" stop-color="var(--crest-light)"/>
            <stop offset="1" stop-color="#b9b6b8"/>
          </linearGradient>
        </defs>
        <path d="M125 0 L250 50 C250 170 220 270 125 332 C30 270 0 170 0 50 Z" fill="var(--crest-dark)"/>
        <path d="M125 16 L234 60 C232 168 205 255 125 312 C45 255 18 168 16 60 Z" fill="url(#crestTone)"/>
      </svg>

      <div class="volume">50cl</div>
      <div class="strength">40% Alc/Vol</div>
    </section>
  </main>
</body>
</html>
```